Car Import Specialist Needs A Flyer

Need a flyer to describe to list the services we provide and cost of those services. We are based in Melbourne ( Australia) but serve customers from all parts of Australia.

The flyer needs to state the following:

Looking for a Japanese performance car? We can find you the car you want and import it for you at the lowest price - Guaranteed!!!!

Why choose us as your direct import partner?

* Over 15 years industry experience
* Vehicles pre-inspection like no other, carried out by our Japan based staff
* Fully licensed motor car trader / QMB 4417 certified / TEVP certified
* In house compliance center
* Mileage guarantee - Export certificates and auction sheets provided with all cars.

-------------------------------------------------------

We need to have pictures of cars on the flyer. I have added pics of cars that we wish to promote.

```html
<!DOCTYPE html>
<html lang="en">
<head>
<meta charset="utf-8">
<title>Japanese Performance Car Import Flyer</title>
<link rel="stylesheet" href="https://fonts.googleapis.com/css2?family=Tinos:wght@700&family=Oswald:wght@400;500&family=Roboto:wght@400;700&display=swap">
<style>
  :root {
    --ink: #121212;
    --ink-soft: #1d1d1d;
    --red: #d9141b;
    --red-deep: #a80c12;
    --white: #ffffff;
    --text-dark: #1a1a1a;
    --serif: "Tinos", "Times New Roman", serif;
    --condensed: "Oswald", "Arial Narrow", sans-serif;
    --sans: "Roboto", Arial, sans-serif;
  }
  html, body {
    margin: 0;
    padding: 0;
    width: 900px;
    height: 1200px;
    overflow: hidden;
    background: #e9e9e9;
  }
  .flyer {
    position: relative;
    width: 900px;
    height: 1200px;
    overflow: hidden;
    background: var(--ink);
  }
  .flyer-shapes {
    position: absolute;
    inset: 0;
    width: 900px;
    height: 1200px;
    display: block;
  }
  .flyer-text { position: absolute; margin: 0; line-height: 1; white-space: nowrap; }

  .brand-company {
    left: 31px; top: 44px;
    font: 700 48px var(--serif);
    color: var(--white);
    letter-spacing: 1px;
  }
  .brand-name {
    left: 29px; top: 99px; width: 289px; height: 48px;
    background: var(--red);
    color: var(--white);
    font: 700 36px var(--sans);
    letter-spacing: 19px;
    display: flex; align-items: center; justify-content: center;
    padding-left: 19px; box-sizing: border-box;
  }

  .headline-lead {
    left: 33px; top: 456px;
    font: 700 36px var(--serif);
    color: var(--red);
  }
  .headline-main {
    left: 31px; top: 500px;
    font: 700 58px var(--serif);
    color: var(--text-dark);
  }
  .headline-tail {
    left: 33px; top: 566px;
    font: 400 52px var(--condensed);
    color: var(--red);
    transform: scaleX(0.9); transform-origin: left;
  }

  .offer-copy {
    left: 30px; top: 678px;
    font: 700 15px/1.45 var(--sans);
    color: var(--white);
  }
  .offer-rule {
    position: absolute;
    left: 30px; top: 724px; width: 316px; height: 2px;
    background: var(--white);
  }
  .offer-guarantee {
    left: 29px; top: 734px;
    font: 500 56px var(--condensed);
    color: var(--white);
    transform: scaleX(0.88); transform-origin: left;
  }

  .call-label {
    left: 33px; top: 908px;
    font: 700 50px var(--serif);
    color: var(--red);
  }
  .call-number {
    left: 29px; top: 966px;
    font: 400 56px var(--condensed);
    color: var(--white);
    transform: scaleX(0.86); transform-origin: left;
  }

  .experience-years {
    right: 35px; top: 612px;
    font: 500 60px var(--condensed);
    color: var(--white);
    transform: scaleX(0.86); transform-origin: right;
  }
  .experience-industry {
    right: 32px; top: 680px;
    font: 700 58px var(--serif);
    color: var(--text-dark);
  }
  .experience-label {
    right: 32px; top: 740px;
    font: 700 48px var(--serif);
    color: var(--white);
  }

  .why-tab {
    right: 30px; top: 826px;
    font: 500 19px var(--condensed);
    color: var(--text-dark);
  }

  .why-list {
    position: absolute;
    right: 32px; top: 886px;
    margin: 0; padding: 0;
    list-style: none;
    text-align: right;
    font: 400 16.5px/21px var(--sans);
    color: var(--white);
    width: 560px;
  }
  .why-list li {
    position: relative;
    padding-right: 24px;
    margin-bottom: 7px;
  }
  .why-list li::after {
    content: "";
    position: absolute;
    right: 0; top: 8px;
    width: 6px; height: 6px;
    border-radius: 50%;
    background: var(--white);
  }

  .contact-line {
    position: absolute;
    top: 1128px;
    display: flex; align-items: center; gap: 14px;
    font: 700 23px var(--serif);
    color: var(--text-dark);
  }
  .contact-address { left: 271px; }
  .contact-web { left: 564px; }
  .contact-icon { width: 20px; height: 22px; display: block; }
</style>
</head>
<body>
<main class="flyer">
  <svg class="flyer-shapes" viewBox="0 0 718 1007" preserveAspectRatio="none" aria-hidden="false">
    <defs>
      <linearGradient id="bg-dark" x1="0" y1="0" x2="1" y2="1">
        <stop offset="0" stop-color="#1a1a1a"/>
        <stop offset="1" stop-color="#0c0c0c"/>
      </linearGradient>
      <linearGradient id="road-photo" x1="0" y1="0" x2="0" y2="1">
        <stop offset="0" stop-color="#a9c6dc"/>
        <stop offset="0.38" stop-color="#dfe6ea"/>
        <stop offset="0.5" stop-color="#6e8a4e"/>
        <stop offset="0.62" stop-color="#4a4d4f"/>
        <stop offset="1" stop-color="#2e3133"/>
      </linearGradient>
      <linearGradient id="showroom-photo" x1="0" y1="0" x2="0" y2="1">
        <stop offset="0" stop-color="#9c9a96"/>
        <stop offset="0.5" stop-color="#e4e2de"/>
        <stop offset="1" stop-color="#b8b6b2"/>
      </linearGradient>
      <linearGradient id="red-panel" x1="0" y1="0" x2="0" y2="1">
        <stop offset="0" stop-color="#de151c"/>
        <stop offset="1" stop-color="#a80c12"/>
      </linearGradient>
    </defs>

    <rect class="backdrop" x="0" y="0" width="718" height="1007" fill="url(#bg-dark)"/>

    <g class="photo-road" role="img" aria-label="Photo of a white hatchback driving along a curved coastal road">
      <polygon points="383,0 718,0 718,415 443,415 296,157" fill="url(#road-photo)" stroke="#ffffff" stroke-width="5" stroke-linejoin="miter"/>
    </g>

    <polygon class="panel-headline" points="0,189 334,189 403,450 358,540 0,540" fill="#ffffff"/>
    <g class="photo-showroom" role="img" aria-label="Photo of a white roadster displayed in a showroom">
      <polygon points="0,195 329,195 373,363 0,363" fill="url(#showroom-photo)"/>
    </g>

    <polygon class="panel-offer" points="0,543 336,543 379,628 336,713 0,713" fill="url(#red-panel)" stroke="#ffffff" stroke-width="4"/>

    <polygon class="panel-experience" points="478,477 718,477 718,897 203,897" fill="url(#red-panel)" stroke="#ffffff" stroke-width="5"/>

    <polygon class="why-tab-shape" points="578,685 718,685 718,723 566,723" fill="#ffffff"/>

    <polygon class="footer-band" points="163,920 718,920 718,1007 123,1007" fill="#ffffff"/>
  </svg>

  <p class="flyer-text brand-company">COMPANY</p>
  <p class="flyer-text brand-name">NAME</p>

  <h1 class="flyer-text headline-lead">LOOKING FOR</h1>
  <p class="flyer-text headline-main">A JAPANESE</p>
  <p class="flyer-text headline-tail">PERFORMANCE CAR?</p>

  <p class="flyer-text offer-copy">WE CAN FIND YOU THE CAR YOU WANT AND<br>IMPORT IT FOR YOU AT THE LOWEST PRICE</p>
  <div class="offer-rule"></div>
  <p class="flyer-text offer-guarantee">GUARANTEED!!</p>

  <p class="flyer-text call-label">CALL US</p>
  <p class="flyer-text call-number">0123456789</p>

  <p class="flyer-text experience-years">OVER 15 YEARS</p>
  <p class="flyer-text experience-industry">INDUSTRY</p>
  <p class="flyer-text experience-label">EXPERIENCE</p>

  <p class="flyer-text why-tab">WHY CHOOSE US</p>
  <ul class="why-list">
    <li>Vehicles pre-inspection like no other, carried out by<br>our Japan based staff</li>
    <li>Fully licensed motor car trader / QMB 4417 certified /<br>TEVP certified</li>
    <li>In house compliance center</li>
    <li>Mileage guarantee - Export certificates and auction sheets<br>provided with all cars.</li>
  </ul>

  <div class="contact-line contact-address">
    <span>YOUR ADDRESS</span>
    <svg class="contact-icon" viewBox="0 0 20 22" aria-hidden="true">
      <path d="M10 1a7 7 0 0 0-7 7c0 5 7 13 7 13s7-8 7-13a7 7 0 0 0-7-7zm0 10a3 3 0 1 1 0-6 3 3 0 0 1 0 6z" fill="#d9141b"/>
    </svg>
  </div>
  <div class="contact-line contact-web">
    <span>YOURWEBSITE.COM</span>
    <svg class="contact-icon" viewBox="0 0 22 22" aria-hidden="true">
      <g fill="none" stroke="#d9141b" stroke-width="1.6">
        <circle cx="11" cy="11" r="9"/>
        <ellipse cx="11" cy="11" rx="4" ry="9"/>
        <line x1="2" y1="11" x2="20" y2="11"/>
        <line x1="3.5" y1="6.5" x2="18.5" y2="6.5"/>
        <line x1="3.5" y1="15.5" x2="18.5" y2="15.5"/>
      </g>
    </svg>
  </div>
</main>
</body>
</html>
```